Hispanic Financial Counseling and Advocate Firm seeks business card design

Looking for a clean, professional business card design. This is a firm that specializes in providing financial education, coaching, and planning to the Hispanic community. The name of the company is Valemar, which means to prosper. We need a design that is clean, professional, and invokes trust, professionalism, but also welcoming. Our logo is a plant growing from a hand to give the messaging of of being in control of growing your financial future and security. Its part of a larger organization names Celesta Financial Group, who's logo is a tree with multi colored branches. We have the back of the card designed so we just need the front designed. the back is blue, so front needs to be a different background color, not blue.

Target Market(s)

Hispanic Community looking to better their future

Industry/Entity Type

financial services

Contact Information for Business Card

contact info: Anselmo Ibarra Jr, 951-555-0147, info@celestafinancialgroup.example. Celestafinancialgroup.example. tag line: Para un futuro mas seguro!

Requirements
Must have
• basics: logo, contact info.
Nice to have
• possibly incorporate the tree logo provided somehow
Should not have
• should not look like the back, needs to be different from the back provided.

```html
<!DOCTYPE html>
<html lang="es">
<head>
<meta charset="utf-8">
<title>Valemar – Tarjeta de presentación</title>
<link href="https://fonts.googleapis.com/css2?family=Red+Hat+Display:wght@400;500;700&family=Roboto:wght@400;500&display=swap" rel="stylesheet">
<style>
  :root {
    --backdrop: #808084;
    --leaf-green: #6aa92f;
    --navy: #002e45;
    --white: #ffffff;
    --bullet-green: #9acb3c;
    --bullet-blue: #2ea3dc;
    --bullet-red: #e8434a;
    --bullet-purple: #a283c4;
    --bullet-yellow: #f6b81c;
  }
  * { margin: 0; padding: 0; box-sizing: border-box; }
  html, body { width: 1200px; height: 800px; overflow: hidden; }
  body { background: var(--backdrop); position: relative; }

  .card { position: absolute; left: 390px; width: 420px; height: 240px; color: var(--white); }
  .card--front { top: 130px; background: var(--leaf-green); font-family: "Red Hat Display", sans-serif; }
  .card--back { top: 430px; background: var(--navy); font-family: "Roboto", sans-serif; }

  .abs { position: absolute; line-height: 1; white-space: nowrap; }

  /* front */
  .brand-mark { left: 55px; top: 68px; width: 100px; height: 100px; border-radius: 50%; background: rgba(255,255,255,0.9); }
  .brand-name { left: 220px; top: 35px; font-size: 35px; font-weight: 500; letter-spacing: -0.3px; }
  .brand-descriptor { left: 221px; top: 67px; font-size: 9px; font-weight: 700; letter-spacing: 1.3px; }
  .holder-name { left: 221px; top: 100px; font-size: 13px; font-weight: 500; letter-spacing: 0.2px; }
  .contact-list { left: 221px; top: 128px; list-style: none; font-size: 10.5px; }
  .contact-item { display: flex; align-items: center; height: 14px; }
  .contact-item svg { width: 9px; height: 9px; margin-right: 5px; fill: var(--white); }
  .tagline { left: 221px; top: 186px; font-size: 10.5px; }

  /* back */
  .parent-mark { left: 47px; top: 36px; width: 100px; height: 100px; border-radius: 50%; background: rgba(255,255,255,0.9); }
  .divider { left: 162px; top: 21px; width: 1px; height: 126px; background: var(--white); }
  .parent-name { left: 180px; top: 64px; font-size: 50px; font-weight: 500; letter-spacing: -1.5px; }
  .parent-suffix { left: 181px; top: 113px; font-size: 19px; font-weight: 500; letter-spacing: 0.5px; }
  .services { left: 0; width: 420px; top: 180px; text-align: center; font-size: 12px; line-height: 15px; }
  .service { display: inline-flex; align-items: center; margin: 0 2px; }
  .service::before { content: ""; width: 4px; height: 7px; border-radius: 50%; margin-right: 3px; background: var(--dot); }
  .service--green { --dot: var(--bullet-green); }
  .service--blue { --dot: var(--bullet-blue); }
  .service--red { --dot: var(--bullet-red); }
  .service--purple { --dot: var(--bullet-purple); }
  .service--yellow { --dot: var(--bullet-yellow); }
</style>
</head>
<body>

<section class="card card--front" aria-label="Frente de la tarjeta">
  <div class="abs brand-mark" aria-hidden="true"></div>
  <div class="abs brand-name">Valemar</div>
  <div class="abs brand-descriptor">SERVICIOS FINANCIEROS</div>
  <div class="abs holder-name">ANSELMO IBARRA JR</div>
  <ul class="abs contact-list">
    <li class="contact-item">
      <svg viewBox="0 0 24 24" aria-hidden="true"><path d="M6.6 10.8a15.1 15.1 0 0 0 6.6 6.6l2.2-2.2a1 1 0 0 1 1-.25 11.4 11.4 0 0 0 3.6.57 1 1 0 0 1 1 1V20a1 1 0 0 1-1 1A17 17 0 0 1 3 4a1 1 0 0 1 1-1h3.5a1 1 0 0 1 1 1c0 1.25.2 2.45.57 3.57a1 1 0 0 1-.25 1z"/></svg>
      951-555-0147
    </li>
    <li class="contact-item">
      <svg viewBox="0 0 24 24" aria-hidden="true"><path d="M2 5h20v14H2z M2 5l10 8 10-8" fill="var(--white)"/><path d="M2 6l10 7 10-7" fill="none" stroke="var(--leaf-green)" stroke-width="2"/></svg>
      info@celestafinancialgroup.example
    </li>
    <li class="contact-item">
      <svg viewBox="0 0 24 24" aria-hidden="true"><g fill="none" stroke="var(--white)" stroke-width="2"><circle cx="12" cy="12" r="10"/><ellipse cx="12" cy="12" rx="4.5" ry="10"/><path d="M2 12h20M4 7h16M4 17h16"/></g></svg>
      Celestafinancialgroup.example
    </li>
  </ul>
  <div class="abs tagline">Para un futuro mas seguro!</div>
</section>

<section class="card card--back" aria-label="Reverso de la tarjeta">
  <div class="abs parent-mark" aria-hidden="true"></div>
  <div class="abs divider" aria-hidden="true"></div>
  <div class="abs parent-name">Celesta</div>
  <div class="abs parent-suffix">Financial Group Inc</div>
  <div class="abs services">
    <div><span class="service service--green">Inmigración</span> <span class="service service--blue">Planificacion Financiera</span></div>
    <div><span class="service service--red">Seguros</span> <span class="service service--purple">Impuestos</span> <span class="service service--red">Y mas</span></div>
    <div><span class="service service--yellow">Preparación de documentos</span></div>
  </div>
</section>

</body>
</html>
```